Refresh look of our invoices (Excel spreadsheet which converts to PDF) to better match our new look

We have recently updated our Website and other marketing material with a new look and would like to refresh our invoice template so that it better matches our new look.  The template is an excel spreadsheet which we convert to a PDF to send out to our clients.
The main requirement is to incorporate the newer design colours and general look/feel to align with what is on our website www.tarvellgroup.com.au
It is extremely important that excel formula functionality and general layout are much the same although we are open to any design suggestions you might have.
Please note:
-Totals figures and news panel must remain on the first page
-We need full ability to edit embedded formulas and Excel spreadsheet is NOT to be password protected as we will only be using it internally.
-It is crucial that the second and subsequent pages can be extended (duplicated) internally to allow for larger multi page entries. Some of our clients invoices run up to 4/5 pages in length and we need the abilty to keep adding rows)
-possibility to add a "convert to PDF" button within the sheet which provides a 1 click solution to convert to PDF rather than the manual 2 step process to convert.... If that can be done, we would not want the "convert to PDF" button to show on final PDF converted version we issue to our customers.   Ideally, a single "convert to PDF and print first cover page only" in 1 single click button named 'convert to PDF & print' would be really handy.  -  (Just to explain why - we email out a PDF version of invoice to our clients and only print off first page with totals for our records)
The design for the first page can be different from the second & subsequent pages (eg first page can be more fancy with following pages more basic)

Finance Industry
Marketing

```html
<!DOCTYPE html>
<html lang="en">
<head>
<meta charset="utf-8">
<title>Tarvell Group – Recipient Created Tax Invoice</title>
<link rel="stylesheet" href="https://fonts.googleapis.com/css2?family=Arimo:wght@400;700&display=swap">
<style>
:root{
  --bg:#e6e6e6;
  --paper:#ffffff;
  --ink:#3a3a3a;
  --ink-soft:#555555;
  --rule:#444444;
  --bar:#3d3d3d;
  --green:#8dc63f;
  --red:#e31e24;
}
*{box-sizing:border-box;margin:0;padding:0}
html,body{width:1040px;height:1200px;overflow:hidden}
body{background:var(--bg);font-family:"Arimo",Arial,sans-serif;color:var(--ink);position:relative}
.page{position:absolute;left:103px;width:834px;height:586px;background:var(--paper);box-shadow:0 1px 4px rgba(0,0,0,.25)}
.page--cover{top:6px}
.page--detail{top:604px}
.abs{position:absolute}

/* cover header */
.brand{left:44px;top:60px;font-size:44px;font-weight:700;letter-spacing:1px;color:#58595b;line-height:1}
.issuer{right:114px;top:54px;text-align:right;font-size:9.5px;font-weight:700;line-height:13px;color:var(--ink)}
.issuer .issuer-name{font-size:12px;line-height:16px}
.issuer .issuer-web{color:var(--green)}
.head-rule{left:48px;top:136px;width:672px;height:3px;background:var(--rule)}
.abn{right:114px;top:146px;font-size:10px;font-weight:700}
.doc-title{left:0;width:768px;top:158px;text-align:center;font-size:14.5px;font-weight:700;color:#444}
.invoice-date{right:182px;top:184px;font-size:9.5px;font-weight:700}
.referrer{left:48px;top:202px;font-size:9.5px;font-weight:700;line-height:17px}
.referrer-abn{left:48px;top:264px;font-size:9.5px;font-weight:700}

/* summary */
.summary{left:540px;top:288px;width:180px;font-size:12px;font-weight:700}
.summary-row{display:flex;justify-content:space-between;height:15.6px;line-height:15.6px}
.summary-row dt{width:84px;text-align:right}
.summary-row dd{text-align:right}
.neg{color:var(--red)}
.summary-total{left:380px;top:350px;width:340px;display:flex;justify-content:space-between;align-items:center;font-size:12px;font-weight:700}
.summary-total .boxed{border:2px solid var(--ink);padding:1px 4px;width:94px;text-align:right}

/* news panel */
.news{left:48px;top:458px;width:674px;font-size:9.5px;font-weight:700;line-height:12px}
.news-title{color:var(--red)}
.news a{color:var(--green);text-decoration:none}
.privacy{left:48px;top:510px;width:674px;border:1.5px solid var(--ink);font-size:7px;font-style:italic;line-height:9px;padding:1px 2px}

/* detail table */
.detail-referrer{left:48px;top:88px;font-size:9.5px;font-weight:700}
.cols{display:grid;grid-template-columns:98px 64px 132px 72px 76px 62px 72px 98px;width:674px;text-align:center}
.table-head{left:48px;top:139px;height:23px;background:var(--bar);color:var(--green);font-size:10px;font-weight:700;align-items:center}
.table-body{left:48px;top:166px;font-size:9.5px;color:var(--ink-soft);line-height:12px}
.notes{left:48px;top:374px;font-size:9px;color:var(--red);line-height:12px}
.notes .note{grid-column:1 / span 5;text-align:left}
.totals-head{left:48px;top:410px;height:17px;background:var(--bar);color:var(--green);font-size:10px;font-weight:700;align-items:center}
.totals-row{left:48px;top:434px;font-size:11px;font-weight:700;align-items:center}
.totals-row .boxed{border:2px solid var(--ink);margin-left:6px;padding:2px 0}
</style>
</head>
<body>

<section class="page page--cover">
  <div class="abs brand">TARVELL GROUP</div>
  <div class="abs issuer">
    <div class="issuer-name">Tarvell Group Pty Ltd</div>
    <div>Level 12, 88 Harbour Street,</div>
    <div>Geelong VIC 3220</div>
    <div class="issuer-web">www.tarvellgroup.com.au</div>
    <div>Ph 1300 555 014 Fax 1300 555 027</div>
    <div>Australian Credit Licence: 400123</div>
  </div>
  <div class="abs head-rule"></div>
  <div class="abs abn">ABN &nbsp;00 111 222 333</div>
  <h1 class="abs doc-title">RECIPIENT CREATED TAX INVOICE</h1>
  <div class="abs invoice-date">Invoice Date: &nbsp;16-Sep-13</div>

  <div class="abs referrer">
    <div>Referrer name</div>
    <div>referrer address line 1</div>
    <div>referrer address line 2</div>
  </div>
  <div class="abs referrer-abn">ABN: 00 000 000 000</div>

  <dl class="abs summary">
    <div class="summary-row"><dt>Upfront</dt><dd>$3,000.00</dd></div>
    <div class="summary-row"><dt>Trail</dt><dd>$202.26</dd></div>
    <div class="summary-row"><dt>Adjustments</dt><dd class="neg">-$50.00</dd></div>
    <div class="summary-row"><dt>GST</dt><dd>$315.24</dd></div>
  </dl>
  <div class="abs summary-total"><span style="margin-left:72px">TOTAL AMOUNT DEPOSITED</span><span class="boxed">$3,467.50</span></div>

  <div class="abs news">
    <div class="news-title">* TARVELL CONNECT - Referral management software *</div>
    <p>The Tarvell Connect software provides you with a fully compliant referral process that is supported by the lenders. Apart from making new referrals, you can also read lender updates on deal progress and lodge enquires for outstanding commission payments. You can login by going to the dedicated Tarvell Connect website at: <a>www.tarvellmembers.com.au</a></p>
  </div>
  <div class="abs privacy">This report contains confidential client information. Disclosure of customer information such as loan details and lenders to third parties may be a contravention of the Privacy Act, unless they are authorised to receive such details.</div>
</section>

<section class="page page--detail">
  <div class="abs detail-referrer">referrer name</div>

  <div class="abs cols table-head">
    <span>Client</span><span>Lender</span><span>Loan Amount</span><span>Upfront</span><span>Trail</span><span>Adj.</span><span>GST</span><span>TOTAL</span>
  </div>

  <div class="abs cols table-body">
    <span>dsgfg</span><span>Eastline</span><span>$34,182.00</span><span>$0.00</span><span>$3.48</span><span>$0.00</span><span>$0.35</span><span>$3.83</span>
    <span>ggffgfd</span><span>Eastline</span><span>$132,583.00</span><span>$0.00</span><span>$13.51</span><span>$0.00</span><span>$1.35</span><span>$14.86</span>
    <span>fggfdfg</span><span>Eastline</span><span>$119,988.00</span><span>$0.00</span><span>$12.23</span><span>$0.00</span><span>$1.22</span><span>$13.45</span>
    <span>gfdfg</span><span>Eastline</span><span>$479,999.00</span><span>$0.00</span><span>$48.92</span><span>$0.00</span><span>$4.89</span><span>$53.81</span>
    <span>dfg</span><span>Eastline</span><span>$134,161.00</span><span>$0.00</span><span>$13.67</span><span>$0.00</span><span>$1.37</span><span>$15.04</span>
    <span>gdfg</span><span>Eastline</span><span>$78,927.00</span><span>$0.00</span><span>$8.05</span><span>$0.00</span><span>$0.81</span><span>$8.86</span>
    <span>dffdgvfgf</span><span>Eastline</span><span>$149,400.00</span><span>$0.00</span><span>$15.22</span><span>$0.00</span><span>$1.52</span><span>$16.74</span>
    <span>fgdg</span><span>Eastline</span><span>$99,805.00</span><span>$0.00</span><span>$10.17</span><span>$0.00</span><span>$1.02</span><span>$11.19</span>
    <span>ffgdggf</span><span>Eastline</span><span>$377,100.00</span><span>$0.00</span><span>$38.43</span><span>$0.00</span><span>$3.84</span><span>$42.27</span>
    <span>df</span><span>Eastline</span><span>$101,738.00</span><span>$0.00</span><span>$10.37</span><span>$0.00</span><span>$1.04</span><span>$11.41</span>
    <span>gdgsdgsdf</span><span>Eastline</span><span>$50,564.00</span><span>$0.00</span><span>$5.15</span><span>$0.00</span><span>$0.52</span><span>$5.67</span>
    <span>dsfggddfg</span><span>Eastline</span><span>$108,500.00</span><span>$0.00</span><span>$7.38</span><span>$0.00</span><span>$0.74</span><span>$8.12</span>
    <span>dfdfgdsfghfd</span><span>Eastline</span><span>$230,807.00</span><span>$0.00</span><span>$15.68</span><span>$0.00</span><span>$1.57</span><span>$17.25</span>
    <span>dfdjsf</span><span>OZB</span><span>$600,000.00</span><span>$3,000.00</span><span>$0.00</span><span>$0.00</span><span>$300.00</span><span>$3,300.00</span>
  </div>

  <div class="abs cols notes">
    <span class="note">- only applies in months with a new settlement occurring</span><span>-$50.00</span><span>-$5.00</span><span>-$55.00</span>
    <span class="note">deducted from trail if <u>no new deals within last 6 months</u></span><span>$0.00</span><span>$0.00</span><span>$0.00</span>
  </div>

  <div class="abs cols totals-head">
    <span></span><span></span><span>Loan Book</span><span>Upfront</span><span>Trail</span><span>Adj.</span><span>GST</span><span>TOTAL</span>
  </div>
  <div class="abs cols totals-row">
    <span></span><span></span><span>$2,697,754.00</span><span>$3,000.00</span><span>$202.26</span><span class="neg">-$50.00</span><span>$315.24</span><span class="boxed">$3,467.50</span>
  </div>
</section>

</body>
</html>
```